Custom Manufacturing Job Shop

We are looking for a business card design for Tall Oak Fabrication Inc. Tall Oak is a family owned business that manufactures any custom product to fit a customers needs, whether it is custom 1 piece or production parts, we truly take on projects that others just cant do. to help in your design go to www.talloakfab.example for a more in depth idea. we have the following capabilities that we would like to see on the card somewhere...maybe on the back of a 2 sided card? we are fully open to ideas.
Machining
• Fabrication
• Millwork
• Maintenance
• Laser Cutting
• Precision Forming
Engineering
Blasting/Painting

No matter how big or small, We literally do it all

preferably black or darker cards but we don't mind to see some color if you see a better fit. we are interested in looking at anything that catches attention.
I have attached our logo, if it is needed in a different file type please let me know and I will send it to you if I can. maybe adding some type of drawing or dimensional lines would be something to add?? just throwing ideas out there....

Reason: I added one of our shredder designs and would like to see a few more cards if possible using this. any questions please don't hesitate to ask!!

Target Market(s)

anyone looking for design/manufacturing/machining whether it is custom 1 off parts or production.

Industry/Entity Type

Business

Contact Information for Business Card

preferably darker shades, but also not opposed to some color in the same sense....not too bright

Font styles to use
Serif
Sans Serif

Requirements
Must have
• Dell Marwick
• Direct:555-213-7790
• Cell:555-348-1162
• Fax: 555-907-4425
• 42 Quarry Lane
• Cedarvale, ST 00000
• I also would request having it in a format I can give to the company making the business cards to edit names/numbers etc. for the entire staff.
Nice to have
• drafting lines? we are open to almost anything....
Should not have
• exotic colors

```html
<!DOCTYPE html>
<html lang="en">
<head>
<meta charset="utf-8">
<title>Tall Oak Fabrication Inc. – Business Card</title>
<link rel="stylesheet" href="https://fonts.googleapis.com/css2?family=Open+Sans:wght@400;600&display=swap">
<style>
  :root {
    --page: #ffffff;
    --card-top: #2b2b2b;
    --card-mid: #151515;
    --card-bottom: #060606;
    --brand: #dcdcdc;
    --url: #c9c9c9;
    --name: #ffffff;
    --detail: #d6d6d6;
    --band-light: #8a8a8a;
    --band-dark: #2e2e2e;
  }
  * { margin: 0; padding: 0; box-sizing: border-box; }
  html, body {
    width: 1200px;
    height: 600px;
    overflow: hidden;
    background: var(--page);
  }
  .card {
    position: absolute;
    left: 5px;
    top: 8px;
    width: 1189px;
    height: 576px;
    border-radius: 24px;
    overflow: hidden;
    background: radial-gradient(ellipse at 30% 25%, var(--card-top) 0%, var(--card-mid) 45%, var(--card-bottom) 100%);
    font-family: "Open Sans", sans-serif;
  }
  .brand {
    position: absolute;
    left: 34px;
    top: 62px;
    width: 780px;
  }
  .brand-name {
    display: block;
    font-weight: 600;
    font-size: 136px;
    line-height: 1.1;
    color: var(--brand);
    text-transform: uppercase;
    white-space: nowrap;
  }
  .brand-url {
    display: block;
    margin-top: 12px;
    text-align: right;
    font-weight: 400;
    font-size: 29px;
    letter-spacing: 5px;
    color: var(--url);
    text-transform: uppercase;
    white-space: nowrap;
  }
  .contact {
    position: absolute;
    left: 847px;
    top: 215px;
    color: var(--detail);
  }
  .contact-name {
    font-weight: 400;
    font-size: 40px;
    line-height: 1.2;
    color: var(--name);
    margin-bottom: 50px;
  }
  .contact-lines {
    list-style: none;
    font-size: 27px;
    line-height: 40px;
    white-space: nowrap;
  }
  .footer-band {
    position: absolute;
    left: 0;
    bottom: 0;
    width: 100%;
    height: 36px;
    background: linear-gradient(180deg, var(--band-dark) 0%, var(--band-light) 100%);
  }
</style>
</head>
<body>
  <div class="card">
    <div class="brand">
      <span class="brand-name">Tall Oak</span>
      <span class="brand-url">talloakfab.example</span>
    </div>

    <div class="contact">
      <p class="contact-name">Dell Marwick</p>
      <ul class="contact-lines">
        <li>Direct:555-213-7790</li>
        <li>Cell:555-348-1162</li>
        <li>Fax: 555-907-4425</li>
        <li>42 Quarry Lane</li>
        <li>Cedarvale, ST 00000</li>
      </ul>
    </div>

    <div class="footer-band" role="img" aria-label="Decorative grey chevron tread pattern band along the bottom edge"></div>
  </div>
</body>
</html>
```